Floristry Business Card Design Project

I have a logo now and am looking to incorporate this into a business card. I would like a double sided business card. I would like one side to be decorative so that it blends well when included with floral arrangements and that can also be used as the front of a card and the other side will contain the business details. The font on the business details side should be clear although some decorative font would be ok. I have included the logo files for use in the business card design.

Feel free to break up the logo and use certain aspects of it in the design. Really looking for something that stands out and that is really creative.

Industry/Entity Type

Floral

Requirements
Should not have
• Nothing tacky or corny. The logo should be clearly read (perhaps a background colour).

```html
<!DOCTYPE html>
<html lang="en">
<head>
<meta charset="utf-8">
<title>Petal Lane – Business Card</title>
<link rel="stylesheet" href="https://fonts.googleapis.com/css2?family=Cinzel:wght@400&display=swap">
<style>
  :root {
    --paper: #ffffff;
    --card-edge: #ececec;
    --salmon: #e09c86;
    --teal: #5aa597;
    --leaf: #b5ca78;
    --leaf-tint: #d8e4ae;
    --salmon-tint: #efbfae;
    --teal-tint: #bcdcd1;
    --disc: #fdfdfd;
  }
  * { margin: 0; padding: 0; box-sizing: border-box; }
  html, body {
    width: 1200px; height: 1000px; overflow: hidden;
    background: var(--paper);
  }
  .sheet { position: relative; width: 1200px; height: 1000px; }
  .card {
    position: absolute; top: 322px; width: 550px; height: 356px;
    border: 1px solid var(--card-edge); overflow: hidden;
    font-family: "Cinzel", "Trajan Pro", serif; font-weight: 400;
  }
  .card--front { left: 30px; }
  .card--back { left: 620px; }
  .card__pattern {
    position: absolute; inset: 0;
    background: linear-gradient(90deg,
      var(--paper) 0px, var(--leaf-tint) 22px, var(--paper) 42px,
      var(--salmon-tint) 60px, var(--paper) 78px,
      var(--leaf-tint) 108px, var(--paper) 132px,
      var(--salmon-tint) 160px, var(--paper) 182px,
      var(--teal-tint) 196px, var(--paper) 208px,
      var(--leaf-tint) 230px, var(--paper) 252px,
      var(--salmon-tint) 276px, var(--paper) 298px,
      var(--leaf-tint) 320px, var(--paper) 342px,
      var(--teal-tint) 356px, var(--paper) 368px,
      var(--salmon-tint) 392px, var(--paper) 414px,
      var(--leaf-tint) 444px, var(--paper) 470px,
      var(--salmon-tint) 492px, var(--paper) 510px,
      var(--leaf-tint) 530px, var(--paper) 550px);
  }
  .card__frame { position: absolute; left: 0; top: 0; width: 550px; height: 356px; }
  .card__line {
    position: absolute; left: 0; width: 550px; text-align: center; white-space: nowrap;
  }
  .brand-dot {
    position: absolute; left: 199px; top: 58px; width: 150px; height: 150px; border-radius: 50%;
    background: radial-gradient(circle, var(--disc) 0 42%, var(--leaf-tint) 62%, var(--salmon-tint) 100%);
  }
  .brand-name {
    top: 241px; color: var(--teal); font-size: 20px; line-height: 1; letter-spacing: 5px;
  }
  .owner-name {
    top: 110px; color: var(--salmon); font-size: 40px; line-height: 1; letter-spacing: 0.5px;
  }
  .owner-role {
    top: 158px; color: var(--leaf); font-size: 15px; line-height: 1; letter-spacing: 4px;
  }
  .contact__phone { top: 206px; color: var(--teal); font-size: 15px; line-height: 1; }
  .contact__email { top: 227px; color: var(--teal); font-size: 14px; line-height: 1; letter-spacing: 0.3px; }
</style>
</head>
<body>
<main class="sheet">

  <section class="card card--front">
    <div class="card__pattern" role="img" aria-label="Repeating pattern of pink flower sprigs and green leafy vines in vertical rows"></div>
    <svg class="card__frame" viewBox="0 0 550 356" aria-hidden="true">
      <circle cx="274" cy="178" r="161" fill="var(--disc)" stroke="var(--salmon)" stroke-width="3"/>
      <circle cx="274" cy="178" r="153" fill="none" stroke="var(--teal)" stroke-width="1.3"/>
    </svg>
    <div class="brand-dot"></div>
    <p class="card__line brand-name">Petal Lane</p>
  </section>

  <section class="card card--back">
    <div class="card__pattern" role="img" aria-label="Repeating pattern of pink flower sprigs and green leafy vines in vertical rows"></div>
    <svg class="card__frame" viewBox="0 0 550 356" aria-hidden="true">
      <circle cx="274" cy="178" r="161" fill="var(--disc)" stroke="var(--salmon)" stroke-width="3"/>
      <circle cx="274" cy="178" r="153" fill="none" stroke="var(--teal)" stroke-width="1.3"/>
    </svg>
    <h1 class="card__line owner-name">Mara Linden</h1>
    <p class="card__line owner-role">FLOWER CREATIONS</p>
    <p class="card__line contact__phone">0400 123 456</p>
    <p class="card__line contact__email">PETALLANE1@EXAMPLE.COM</p>
  </section>

</main>
</body>
</html>
```